Harbor Pine builders of ny Roofing flyer

We would like to create a flyer for roofing customers : commercial / real estate management / business / schools /warehouses

Flat roof specialists
Waterproofing experts

Special flat roof re layer @ 3.00 per sq ft

Roof leak repairs
Flashing
Waterproofing

Call 555 3019462

For pictures find torch down roof applications
Flat roofs ny

```html
<!DOCTYPE html>
<html lang="en">
<head>
<meta charset="utf-8">
<title>Harbor Pine Builders of NY Roofing Flyer</title>
<link href="https://fonts.googleapis.com/css2?family=Bebas+Neue&family=Montserrat:wght@700;800&family=Playfair+Display:wght@400&display=swap" rel="stylesheet">
<style>
  :root {
    --sky-blue: #2fb0e6;
    --strip-blue: #1ba6e4;
    --navy: #1b2f73;
    --navy-deep: #142463;
    --red: #c8102e;
    --band-dark: rgba(40, 42, 46, 0.88);
    --ink: #2b2b2b;
    --white: #ffffff;
  }
  * { margin: 0; padding: 0; box-sizing: border-box; }
  html, body { width: 900px; height: 1200px; overflow: hidden; background: #ffffff; }
  .flyer { position: relative; width: 900px; height: 1200px; overflow: hidden; background: var(--white); }

  .hero-photo {
    position: absolute; left: 0; top: 0; width: 900px; height: 863px;
    background: linear-gradient(180deg, #dfe6ec 0%, #c9d3dc 40%, #8f969e 62%, #5c6168 80%, #45494f 100%);
  }
  .headline-circle {
    position: absolute; left: -60px; top: -125px; width: 520px; height: 520px;
    border-radius: 50%; background: var(--sky-blue);
  }
  .headline {
    position: absolute; left: 50px; top: 40px;
    font-family: "Bebas Neue", sans-serif; color: var(--white);
    font-size: 98px; line-height: 87px; letter-spacing: 0.5px;
  }
  .company-name {
    position: absolute; left: 557px; top: 52px;
    font-family: "Playfair Display", serif; color: var(--ink);
    font-size: 30px; line-height: 40px;
  }

  .specialty-band {
    position: absolute; left: 0; top: 712px; width: 900px; height: 151px;
    background: var(--band-dark);
  }
  .specialty-band .line {
    position: absolute; left: 50px;
    font-family: "Bebas Neue", sans-serif; font-size: 60px; line-height: 1;
  }
  .specialty-band .line-blue { top: 18px; color: var(--strip-blue); }
  .specialty-band .line-white { top: 78px; color: var(--white); }

  .offer-badge { position: absolute; left: 626px; top: 653px; width: 236px; height: 236px; }
  .offer-badge text { font-family: "Montserrat", sans-serif; font-weight: 800; }

  .services {
    position: absolute; left: 0; top: 863px; width: 900px; height: 184px;
    display: flex; align-items: center;
  }
  .service {
    flex: 1; height: 100%; display: flex; flex-direction: column; align-items: center;
    justify-content: center; gap: 10px;
    font-family: "Montserrat", sans-serif; font-weight: 700; color: var(--ink);
    font-size: 21px; line-height: 27px; text-align: center;
  }
  .service-divider { width: 1.5px; height: 92px; background: var(--ink); margin-top: 36px; }
  .service svg { width: 64px; height: 64px; }

  .contact-strip {
    position: absolute; left: 0; top: 1047px; width: 900px; height: 38px;
    background: var(--strip-blue); display: flex; align-items: center; justify-content: center; gap: 18px;
    font-family: "Montserrat", sans-serif; font-weight: 700; color: var(--white); font-size: 16.5px;
  }
  .contact-strip .rule { width: 58px; height: 1.5px; background: var(--white); }

  .call-block {
    position: absolute; left: 0; top: 1085px; width: 900px; height: 115px;
    background: linear-gradient(180deg, var(--navy) 0%, var(--navy-deep) 100%);
    color: var(--white); font-family: "Montserrat", sans-serif; font-weight: 800;
  }
  .call-line {
    position: absolute; left: 0; right: 0; top: 10px; display: flex; align-items: center; justify-content: center; gap: 20px;
    font-size: 46px; letter-spacing: 0.5px;
  }
  .call-line svg { width: 34px; height: 34px; }
  .web-line {
    position: absolute; left: 0; right: 0; top: 80px; display: flex; align-items: center; justify-content: center; gap: 18px;
    font-size: 18px; font-weight: 700;
  }
  .web-line svg { width: 18px; height: 18px; }
</style>
</head>
<body>
<div class="flyer">
  <div class="hero-photo" role="img" aria-label="Photo of two roofers in hard hats nailing asphalt shingles on a roof under a cloudy sky"></div>

  <div class="headline-circle"></div>
  <h1 class="headline">NEED A<br>ROOFING<br>EXPERTS?</h1>

  <p class="company-name">Harbor Pine Builders<br>OF NY Roofing</p>

  <div class="specialty-band">
    <div class="line line-blue">FLAT ROOF SPECIALISTS</div>
    <div class="line line-white">WATERPROOFING EXPERTS</div>
  </div>

  <svg class="offer-badge" viewBox="0 0 236 236" aria-label="Special flat roof re layer at 3.00 per square foot">
    <defs>
      <clipPath id="badge-clip"><circle cx="118" cy="118" r="108"/></clipPath>
    </defs>
    <circle cx="118" cy="118" r="118" fill="#ffffff"/>
    <g clip-path="url(#badge-clip)">
      <rect x="0" y="0" width="236" height="236" fill="#c8102e"/>
      <rect x="0" y="102" width="236" height="62" fill="#26272b"/>
    </g>
    <text x="118" y="42" text-anchor="middle" fill="#ffffff" font-size="21">SPECIAL</text>
    <text x="118" y="66" text-anchor="middle" fill="#ffffff" font-size="21">FLAT ROOF</text>
    <text x="118" y="90" text-anchor="middle" fill="#ffffff" font-size="21">RE LAYER</text>
    <text x="118" y="152" text-anchor="middle" fill="#ffffff" font-size="46">@3.00</text>
    <text x="118" y="192" text-anchor="middle" fill="#ffffff" font-size="19" font-weight="700">per sq/ft</text>
  </svg>

  <section class="services">
    <div class="service">
      <svg viewBox="0 0 64 64" aria-hidden="true">
        <path d="M6 30 L30 12 L48 25" fill="none" stroke="#c8102e" stroke-width="5" stroke-linejoin="miter"/>
        <path d="M14 28 V50 M44 34 V50" stroke="#c8102e" stroke-width="5"/>
        <path d="M50 22 C50 22 44 30 44 33 a6 6 0 0 0 12 0 C56 30 50 22 50 22 Z" fill="#c8102e"/>
        <path d="M40 34 C40 34 36 39 36 41 a4 4 0 0 0 8 0 C44 39 40 34 40 34 Z" fill="#c8102e"/>
      </svg>
      <span>ROOF LEAK<br>REPAIRS</span>
    </div>
    <div class="service-divider"></div>
    <div class="service">
      <svg viewBox="0 0 64 64" aria-hidden="true">
        <g stroke="#c8102e" stroke-width="2" stroke-linecap="round">
          <line x1="32" y1="2" x2="32" y2="9"/><line x1="32" y1="55" x2="32" y2="62"/>
          <line x1="2" y1="32" x2="9" y2="32"/><line x1="55" y1="32" x2="62" y2="32"/>
          <line x1="11" y1="11" x2="16" y2="16"/><line x1="48" y1="48" x2="53" y2="53"/>
          <line x1="53" y1="11" x2="48" y2="16"/><line x1="16" y1="48" x2="11" y2="53"/>
          <line x1="20" y1="4" x2="22" y2="10"/><line x1="44" y1="4" x2="42" y2="10"/>
          <line x1="20" y1="60" x2="22" y2="54"/><line x1="44" y1="60" x2="42" y2="54"/>
        </g>
        <path d="M36 14 L22 35 H31 L27 50 L42 28 H33 Z" fill="#c8102e"/>
      </svg>
      <span>FLASHING</span>
    </div>
    <div class="service-divider"></div>
    <div class="service">
      <svg viewBox="0 0 64 64" aria-hidden="true">
        <path d="M32 4 L54 12 V30 C54 45 44 54 32 60 C20 54 10 45 10 30 V12 Z" fill="none" stroke="#c8102e" stroke-width="3"/>
        <path d="M32 18 C32 18 23 30 23 36 a9 9 0 0 0 18 0 C41 30 32 18 32 18 Z" fill="#c8102e"/>
        <path d="M28 36 L31 39 L37 32" fill="none" stroke="#ffffff" stroke-width="2.5"/>
      </svg>
      <span>WATER<br>PROOFING</span>
    </div>
  </section>

  <div class="contact-strip">
    <span class="rule"></span>
    <span>FOR MORE INFORMATION, PLEASE CONTACT US TODAY</span>
    <span class="rule"></span>
  </div>

  <footer class="call-block">
    <div class="call-line">
      <svg viewBox="0 0 34 34" aria-hidden="true">
        <rect x="1" y="1" width="32" height="32" rx="7" fill="#ffffff"/>
        <path d="M12 7 L15 7 L16 13 L13 15 C14 19 15 21 19 24 L21 21 L27 23 L27 26 C27 28 25 29 23 29 C14 27 8 20 7 11 C7 9 9 7 12 7 Z" fill="#1b2f73"/>
      </svg>
      <span>CALL US :&nbsp; 555 3019 462</span>
    </div>
    <div class="web-line">
      <svg viewBox="0 0 18 18" aria-hidden="true" fill="none" stroke="#ffffff" stroke-width="1.2">
        <circle cx="9" cy="9" r="8"/><ellipse cx="9" cy="9" rx="3.5" ry="8"/>
        <line x1="1" y1="9" x2="17" y2="9"/><line x1="2.5" y1="5" x2="15.5" y2="5"/><line x1="2.5" y1="13" x2="15.5" y2="13"/>
      </svg>
      <span>VISIT : WWW.HARBORPINEROOFING.COM</span>
    </div>
  </footer>
</div>
</body>
</html>
```